Business card for different employees

A professional new updated design incorporating our current business's color themes and styles such as our on-site service trucks decals included in pictures attached. Our current business card is very simple and not professionally designed. We are a small family business but want a professional corporate look.

Target Market(s)

Cards to be handed out to new customers , corperate meetings. For our on site service operators.

Industry/Entity Type

Hydraulic

Contact Information for Business Card

Address, website, phone number, email, logo.
slogan - "Industry chosen hose and fittings provider".
24/7 on-site service , supply and hose management
Experienced , indpendant , family owned

Font styles to use
Sans Serif

Requirements
Must have
• Easily editable so that I can add different names and different roles for employees etc.
Nice to have
• Freedom with colour doesn't necessarily have to be blue but that is our company colour theme with trucks and logo so makes sense for the card to have blue like the trucks.

```html
<!DOCTYPE html>
<html lang="en">
<head>
<meta charset="utf-8">
<title>Keystone Hose and Fittings – Business Card</title>
<link rel="stylesheet" href="https://fonts.googleapis.com/css2?family=Michroma&family=Saira+Condensed:ital,wght@0,500;1,500&family=Roboto:wght@300;400&display=swap">
<style>
  :root{
    --blue:#2f47a8;
    --blue-deep:#242f86;
    --blue-bright:#3a55c4;
    --black:#0d0d0f;
    --white:#ffffff;
    --silver:#dfe4f2;
    --page:#e9eaee;
  }
  *{box-sizing:border-box;margin:0;padding:0}
  html,body{width:1200px;height:900px;overflow:hidden;background:var(--page)}
  body{display:flex;flex-direction:column;align-items:center;justify-content:center;gap:30px}
  .card{position:relative;width:720px;height:411px;overflow:hidden;
    background:linear-gradient(135deg,var(--blue-bright),var(--blue) 45%,var(--blue-deep));
    box-shadow:0 8px 24px rgba(0,0,0,.25);font-family:"Roboto",sans-serif;color:var(--white)}
  .band-white{position:absolute;left:0;right:0;background:var(--white)}
  .band-black{position:absolute;left:0;right:0;background:var(--black)}
  .brand{position:absolute;display:flex;align-items:center;gap:18px}
  .brand-dot{width:86px;height:86px;border-radius:50%;background:var(--black);flex:none}
  .brand-name{font-family:"Michroma",sans-serif;color:var(--blue);font-size:25px;line-height:1.15;letter-spacing:1px}
  .slogan{font-family:"Michroma",sans-serif;font-size:9px;letter-spacing:.5px;color:var(--white);
    background:var(--blue);padding:3px 10px;margin-top:6px;display:inline-block}
  /* front */
  .front .band-white.top{top:0;height:112px}
  .front .brand{left:34px;top:12px}
  .front .band-black.services{top:112px;height:44px;display:flex;align-items:center;padding-left:34px;
    font-family:"Michroma",sans-serif;font-size:17px;letter-spacing:1.5px}
  .details{position:absolute;left:34px;top:174px;right:34px}
  .person{font-family:"Michroma",sans-serif;font-size:22px;letter-spacing:1.5px}
  .role{font-family:"Michroma",sans-serif;font-size:12px;letter-spacing:1.5px;margin-top:4px}
  .contact{display:flex;gap:22px;margin-top:16px;font-size:13px;font-weight:300}
  .contact span{display:flex;align-items:center;gap:6px}
  .address{font-size:13px;font-weight:300;margin-top:6px}
  .hotline{display:flex;align-items:center;gap:12px;margin-top:14px;
    font-family:"Saira Condensed",sans-serif;font-style:italic;font-size:24px}
  .front .band-white.bottom{bottom:0;height:50px;display:flex;align-items:center;gap:22px;padding-left:34px;
    color:var(--black);font-family:"Saira Condensed",sans-serif;font-style:italic;font-size:17px;text-transform:uppercase}
  .front .band-white.bottom span{display:flex;align-items:center;gap:6px}
  .ring{width:11px;height:11px;border-radius:50%;border:2px dotted var(--blue);display:inline-block}
  /* back */
  .back .band-white.top{top:0;height:118px}
  .back .brand{left:40px;top:16px}
  .industries{position:absolute;top:140px;left:34px;right:34px;display:flex;justify-content:space-between}
  .industries ul{list-style:none;font-family:"Michroma",sans-serif;font-size:13px;letter-spacing:1px;line-height:1.9}
  .industries li{display:flex;align-items:center;gap:9px}
  .industries li::before{content:"";width:9px;height:9px;border-radius:50%;border:2px dotted var(--white)}
  .big-phone{position:absolute;left:34px;top:262px;display:flex;align-items:center;gap:14px;
    font-family:"Saira Condensed",sans-serif;font-style:italic;font-size:46px;color:var(--silver)}
  .back .band-black.web{bottom:0;height:62px;display:flex;align-items:center;justify-content:center;
    font-family:"Michroma",sans-serif;font-size:17px;letter-spacing:9px}
</style>
</head>
<body>

<section class="card front" aria-label="Business card front">
  <div class="band-white top">
    <div class="brand">
      <div class="brand-dot"></div>
      <div>
        <div class="brand-name">KEYSTONE<br>HOSE AND FITTINGS</div>
        <div class="slogan">INDUSTRY CHOSEN HOSE AND FITTINGS PROVIDER</div>
      </div>
    </div>
  </div>
  <div class="band-black services">SALES, SUPPLY AND HOSE MANAGEMENT</div>
  <div class="details">
    <div class="person">MARK ELLISON</div>
    <div class="role">MANAGING DIRECTOR</div>
    <div class="contact">
      <span><svg width="10" height="14" viewBox="0 0 10 14"><rect x="1" y="1" width="8" height="12" rx="1.5" fill="none" stroke="#fff" stroke-width="1.4"/></svg>0400 555 019</span>
      <span><svg width="13" height="13" viewBox="0 0 14 14"><circle cx="7" cy="7" r="6" fill="none" stroke="#fff" stroke-width="1.3"/><path d="M1 7h12M7 1c3 3 3 9 0 12M7 1c-3 3-3 9 0 12" fill="none" stroke="#fff" stroke-width="1"/></svg>www.keystonehose.com.au</span>
      <span><svg width="14" height="10" viewBox="0 0 14 10"><rect x=".7" y=".7" width="12.6" height="8.6" fill="none" stroke="#fff" stroke-width="1.3"/><path d="M1 1l6 5 6-5" fill="none" stroke="#fff" stroke-width="1.3"/></svg>info@keystonehose.com.au</span>
    </div>
    <div class="address">42 Carrow Road, Elmsfield, South Australia 5999</div>
    <div class="hotline">
      <svg width="36" height="36" viewBox="0 0 36 36"><path d="M30 10A14 14 0 1 0 32 20" fill="none" stroke="#fff" stroke-width="2.5"/><path d="M28 4l3 7-7 1" fill="none" stroke="#fff" stroke-width="2.5"/><text x="18" y="23" text-anchor="middle" font-family="Roboto,sans-serif" font-size="11" fill="#fff">24</text></svg>
      <span>0400 555 273 &nbsp;24/7 ON-SITE SERVICE</span>
    </div>
  </div>
  <div class="band-white bottom">
    <span><i class="ring"></i>Experienced</span>
    <span><i class="ring"></i>Independant</span>
    <span><i class="ring"></i>Family owned</span>
  </div>
</section>

<section class="card back" aria-label="Business card back">
  <div class="band-white top">
    <div class="brand">
      <div class="brand-dot"></div>
      <div>
        <div class="brand-name">KEYSTONE<br>HOSE AND FITTINGS</div>
        <div class="slogan">INDUSTRY CHOSEN HOSE AND FITTINGS PROVIDER</div>
      </div>
    </div>
  </div>
  <div class="industries">
    <ul><li>TRANSPORT</li><li>MINING</li><li>AGRICULTURE</li></ul>
    <ul><li>CONSTRUCTION</li><li>INDUSTRIAL</li><li>MARINE</li></ul>
    <ul><li>FOOD &amp; BEVERAGE</li><li>EARTHMOVING</li><li>MANUFACTURING</li></ul>
  </div>
  <div class="big-phone">
    <svg width="52" height="52" viewBox="0 0 36 36"><path d="M30 10A14 14 0 1 0 32 20" fill="none" stroke="#dfe4f2" stroke-width="2.5"/><path d="M28 4l3 7-7 1" fill="none" stroke="#dfe4f2" stroke-width="2.5"/><text x="18" y="23" text-anchor="middle" font-family="Roboto,sans-serif" font-size="11" fill="#dfe4f2">24</text></svg>
    <span>(24/7): 0400 555 273</span>
  </div>
  <div class="band-black web">WWW.KEYSTONEHOSE.COM.AU</div>
</section>

</body>
</html>
```